Legal Service Estimated Retainer and Average Case Value

We need an 11x14 flyer that contains the standard retainers and average cost be case, both provided in documents, for each case type we handle. We need the information displayed, preferably in a way that makes the information readable but less troubling to a client shocked at price of litigation. We need one sheet with the retainers and average case value merged into one table.

Target Market(s)

Potential Clients

Font styles to use
Serif
Sans Serif

```html
<!DOCTYPE html>
<html lang="en">
<head>
<meta charset="utf-8">
<title>Average Fee Per Case Type — The Law Office of Morgan T Whitfield</title>
<link rel="stylesheet" href="https://fonts.googleapis.com/css2?family=Cinzel:wght@600&family=Montserrat:wght@400;600;700&display=swap">
<style>
  :root {
    --navy: #11153f;
    --ink: #1c1c2a;
    --row-alt: #f4f4f6;
    --rule: #8a8a8f;
    --paper: #ffffff;
    --sky: #d8e9f6;
    --stone: #e6d8bf;
    --stone-deep: #cdb994;
  }
  * { box-sizing: border-box; margin: 0; padding: 0; }
  html, body { width: 971px; height: 1200px; overflow: hidden; background: var(--paper); }
  body { font-family: "Montserrat", Arial, sans-serif; color: var(--ink); }

  .flyer { position: relative; width: 971px; height: 1200px; background: var(--paper); overflow: hidden; }

  .hero-photo {
    position: absolute; left: 0; top: 0; width: 971px; height: 300px;
    background:
      linear-gradient(180deg, rgba(255,255,255,0) 70%, rgba(255,255,255,0.9) 100%),
      linear-gradient(100deg, var(--sky) 0%, #f4f6f4 30%, var(--stone) 60%, #ddd0b6 80%, var(--stone-deep) 100%);
  }
  .footer-photo {
    position: absolute; left: 0; bottom: 0; width: 971px; height: 190px;
    background:
      linear-gradient(180deg, rgba(255,255,255,1) 0%, rgba(255,255,255,0.55) 45%, rgba(255,255,255,0) 100%),
      linear-gradient(90deg, var(--stone) 0%, #efe6d4 40%, #f1e9d9 60%, var(--stone) 100%);
  }

  .brand {
    position: absolute; left: 145px; top: 84px;
    display: flex; align-items: center; gap: 22px;
  }
  .brand-mark { width: 120px; height: 120px; background: var(--navy); flex: none; }
  .brand-name { font-family: "Cinzel", "Times New Roman", serif; font-weight: 600; color: var(--navy); line-height: 1; }
  .brand-name .lead { display: block; font-size: 23px; letter-spacing: 0.5px; margin-bottom: 4px; }
  .brand-name .name { display: block; font-size: 44px; letter-spacing: 0.5px; }

  .band {
    position: absolute; left: 44px; width: 884px;
    background: var(--navy); color: #fff;
    font-weight: 700; display: flex; align-items: center; padding-left: 16px;
  }
  .band-fees { top: 278px; height: 49px; font-size: 22px; }
  .band-retainers { top: 703px; height: 54px; font-size: 23px; }

  .intro {
    position: absolute; left: 59px; top: 342px; width: 855px;
    font-size: 15.5px; line-height: 19px; color: var(--ink);
  }

  .rate-table {
    position: absolute; left: 44px; width: 884px;
    border-collapse: collapse; font-size: 12px;
    border-bottom: 1px solid var(--rule);
  }
  .rate-table td { height: 20.7px; padding: 0; vertical-align: middle; }
  .rate-table tr:nth-child(odd) td { background: var(--row-alt); }
  .rate-table .case { padding-left: 15px; }
  .fee-table { top: 412px; }
  .fee-table .case { width: 450px; }
  .retainer-table { top: 759px; }
  .retainer-table td { height: 20.5px; }
  .retainer-table .case { width: 384px; }
  .retainer-table .label { width: 66px; text-align: right; padding-right: 16px; }

  .contact { position: absolute; left: 0; width: 971px; text-align: center; color: var(--navy); }
  .phone { top: 1060px; font-size: 36px; font-weight: 700; }
  .address { top: 1103px; font-size: 16.5px; font-weight: 600; color: var(--ink); letter-spacing: 0.2px; }
  .web { top: 1124px; font-size: 37px; font-weight: 700; }
</style>
</head>
<body>
<main class="flyer">
  <div class="hero-photo" role="img" aria-label="Photograph of tall classical stone columns on a courthouse facade against a pale sky"></div>
  <div class="footer-photo" role="img" aria-label="Faded photograph of courthouse stone columns"></div>

  <header class="brand">
    <div class="brand-mark"></div>
    <div class="brand-name">
      <span class="lead">THE LAW OFFICE OF</span>
      <span class="name">MORGAN T WHITFIELD</span>
    </div>
  </header>

  <h2 class="band band-fees">Average Fee Per Case Type</h2>
  <p class="intro">In order for our clients to set expectations for legal fees, we provide the national average range of fees per case type. These are only to provide you with an understanding of what other cases have cost clients in similar cases. Please note these are not estimates nor guarantees of your own legal costs.</p>

  <table class="rate-table fee-table">
    <tr><td class="case">Custody Contempt/Modification</td><td>$5,000 - $8,000</td></tr>
    <tr><td class="case">Custody Initial Order</td><td>$4,000 - $7,000</td></tr>
    <tr><td class="case">Custody &amp; Support</td><td>$5,000 - $8,000</td></tr>
    <tr><td class="case">Support</td><td>$2,000 - $4,000</td></tr>
    <tr><td class="case">Divorce (3301c)</td><td>$1,500 - $3,000</td></tr>
    <tr><td class="case">Divorce (3301d)</td><td>$2,000 - $3,000</td></tr>
    <tr><td class="case">Protection from Abuse</td><td>$1,500 - $3,000</td></tr>
    <tr><td class="case">Divorce &amp; Custody</td><td>$5,000 - $8,000</td></tr>
    <tr><td class="case">Divorce &amp; Equitable Distribution</td><td>$6,000 - $10,000</td></tr>
    <tr><td class="case">Divorce, Custody &amp; Support</td><td>$8,000 - $12,000</td></tr>
    <tr><td class="case">Divorce, Equitable Distribution &amp; Custody</td><td>$10,000 - $15,000</td></tr>
    <tr><td class="case">Divorce, Equitable Distribution &amp; Support</td><td>$8,000 - $12,000</td></tr>
    <tr><td class="case">Divorce, Equitable Distribution, Custody &amp; Support</td><td>$12,000 - $15,000</td></tr>
  </table>

  <h2 class="band band-retainers">Retainers and Total Estimated Case Costs</h2>

  <table class="rate-table retainer-table">
    <tr><td class="case">Divorce (3301 C):</td><td class="label">Retainer:</td><td>$2,000</td></tr>
    <tr><td class="case">Divorce (3301 D):</td><td class="label">Retainer:</td><td>$2,500</td></tr>
    <tr><td class="case">Divorce and Custody:</td><td class="label">Retainer:</td><td>$3,500</td></tr>
    <tr><td class="case">Divorce and Equitable Distribution:</td><td class="label">Retainer:</td><td>$3,500</td></tr>
    <tr><td class="case">Divorce and Support:</td><td class="label">Retainer:</td><td>$3,000</td></tr>
    <tr><td class="case">Divorce, Custody and Support:</td><td class="label">Retainer:</td><td>$3,500</td></tr>
    <tr><td class="case">Divorce, Equitable Distribution and Support:</td><td class="label">Retainer:</td><td>$3,500</td></tr>
    <tr><td class="case">Divorce, Equitable Distribution and Custody:</td><td class="label">Retainer:</td><td>$5,000</td></tr>
    <tr><td class="case">Divorce, Equitable Distribution, Custody and Support:</td><td class="label">Retainer:</td><td>$3,500</td></tr>
    <tr><td class="case">Custody Initial Order:</td><td class="label">Retainer:</td><td>$3,000</td></tr>
    <tr><td class="case">Custody Modification:</td><td class="label">Retainer:</td><td>$3,500</td></tr>
    <tr><td class="case">Custody and Support:</td><td class="label">Retainer:</td><td>$3,000</td></tr>
    <tr><td class="case">(PFA) Protection From Abuse:</td><td class="label"></td><td>$2,000 Paid In Full</td></tr>
  </table>

  <p class="contact phone">(555) 014-2836</p>
  <p class="contact address">4120 BROOKMERE AVENUE, SUITE 204, MILLBROOK, PA 17650</p>
  <p class="contact web">www.morganwhitfieldlaw.com</p>
</main>
</body>
</html>
```